Water Filtration Company needs a business card design using our existing logo/colours!

We design and manufacture and export specialised water filtration equipment. Our equipment will take unclean dirty water and filters to safe clean drinkable water.
We would like to see designs using our existing logo and colours (see attached "Palette") that represents clean safe drinking water (fresh, clean designs but still professional and modern). Our customers are other businesses who supply water filtration equipment, governments, and private individuals.
BUSINESS CARD DETAILS (Common details):
Tel: + 61 7 55 914 372
www: brenvalegroup.com.au
Address: 3/41 Corbett Lane
Kellow Ridge NSW 2517 Australia
(please include the word Australia as we are an international company)
Must include: COMMERCIAL WATER FILTRATION EQUIPMENT
NAME NO 1:
Dennis Harper
General Manager
Mobile: +61 418 27 93 40
Email: dennis@brenvalegroup.com.au
NAME NO. 2:
Karen Poe
Business Manager
Mobile: +61 416 572 814
Email: karen@brenvalegroup.com.au
Must Have:
1) PRINT READY IN .AI & .PDF FORMATS
2) Also saved in file format .ai (Adobe Illustrator - compatible with CS4)
3) Use existing LOGO & COLOURS: Please use our logo (see attached file)
4) FONTS: we have used Avenir & Helvetica in the past but are open to other font types for the address etc.
Thank you!

```html
<!DOCTYPE html>
<html lang="en">
<head>
<meta charset="utf-8">
<title>Brenvale – Business Card</title>
<link rel="stylesheet" href="https://fonts.googleapis.com/css2?family=Exo+2:wght@400;500;600;700&display=swap">
<style>
  :root {
    --bg: #e9ecee;
    --card: #ffffff;
    --teal: #1c7fa3;
    --blue-light: #3aa3c9;
    --blue-mid: #1f7ea6;
    --blue-deep: #0d5a80;
    --swoosh: #9aa1a7;
    --ink: #2b2f33;
    --white: #ffffff;
  }
  * { margin: 0; padding: 0; box-sizing: border-box; }
  html, body {
    width: 1200px; height: 900px; overflow: hidden;
    background: var(--bg);
    font-family: "Exo 2", sans-serif;
  }
  .stage {
    width: 1200px; height: 900px;
    display: flex; align-items: center; justify-content: center; gap: 40px;
  }
  .card {
    position: relative;
    width: 540px; height: 310px;
    background: var(--card);
    border-radius: 28px;
    overflow: hidden;
    box-shadow: 0 10px 30px rgba(0,0,0,.12);
  }
  .card__wave { position: absolute; inset: 0; }
  .brand {
    display: flex; align-items: center; gap: 8px;
    color: var(--teal); font-weight: 600; letter-spacing: .5px; line-height: 1;
  }
  .brand__dot { border-radius: 50%; background: var(--teal); }
  .tagline {
    color: var(--ink); font-weight: 500; text-transform: uppercase; line-height: 1;
  }
  .masthead { position: absolute; left: 30px; top: 30px; }
  .card--front .brand { font-size: 40px; }
  .card--front .brand__dot { width: 14px; height: 14px; }
  .card--front .tagline { font-size: 8.5px; letter-spacing: 1px; margin-top: 7px; }
  .person { position: absolute; right: 32px; top: 68px; text-align: right; color: var(--ink); }
  .person__name { font-size: 19px; font-weight: 600; letter-spacing: 1px; text-transform: uppercase; }
  .person__role { font-size: 14px; margin-top: 3px; }
  .contacts {
    position: absolute; right: 30px; top: 178px;
    list-style: none; color: var(--white); font-size: 12.5px;
    text-align: right;
  }
  .contacts li { display: flex; justify-content: flex-end; align-items: center; gap: 8px; height: 19px; }
  .contacts svg { width: 11px; height: 11px; flex: none; }
  .address {
    position: absolute; left: 30px; right: 30px; bottom: 18px;
    color: var(--white); font-size: 13px; font-weight: 500; letter-spacing: .3px; text-align: center;
  }
  .card--back { display: flex; align-items: center; justify-content: center; }
  .card--back .masthead { position: static; display: flex; flex-direction: column; align-items: center; }
  .card--back .brand { font-size: 78px; gap: 14px; }
  .card--back .brand__dot { width: 26px; height: 26px; }
  .card--back .tagline { font-size: 14px; letter-spacing: 2px; margin-top: 14px; }
</style>
</head>
<body>
<main class="stage">
  <section class="card card--front" aria-label="Business card front">
    <svg class="card__wave" viewBox="0 0 540 310" preserveAspectRatio="none" aria-hidden="true">
      <defs>
        <radialGradient id="blueFill" cx="0.3" cy="0.55" r="0.8">
          <stop offset="0" stop-color="#3aa3c9"/>
          <stop offset="0.55" stop-color="#1f7ea6"/>
          <stop offset="1" stop-color="#0d5a80"/>
        </radialGradient>
      </defs>
      <path d="M0,132 Q250,62 540,168" fill="none" stroke="#9aa1a7" stroke-width="7"/>
      <path d="M0,142 Q250,76 540,178 L540,310 L0,310 Z" fill="url(#blueFill)"/>
    </svg>

    <div class="masthead">
      <div class="brand"><span>Brenvale</span><span class="brand__dot"></span></div>
      <p class="tagline">Commercial Water Filtration Equipment</p>
    </div>

    <div class="person">
      <p class="person__name">Dennis Harper</p>
      <p class="person__role">General Manager</p>
    </div>

    <ul class="contacts">
      <li>+ 61 7 55 914 372
        <svg viewBox="0 0 24 24"><path fill="currentColor" d="M6.6 10.8a15 15 0 0 0 6.6 6.6l2.2-2.2c.3-.3.7-.4 1-.2 1.1.4 2.3.6 3.6.6.6 0 1 .4 1 1V20c0 .6-.4 1-1 1A17 17 0 0 1 3 4c0-.6.4-1 1-1h3.5c.6 0 1 .4 1 1 0 1.3.2 2.5.6 3.6.1.3 0 .7-.2 1z"/></svg>
      </li>
      <li>+61 418 27 93 40
        <svg viewBox="0 0 24 24"><rect x="6" y="2" width="12" height="20" rx="2" fill="none" stroke="currentColor" stroke-width="2"/><circle cx="12" cy="18" r="1.3" fill="currentColor"/></svg>
      </li>
      <li>dennis@brenvalegroup.com.au
        <svg viewBox="0 0 24 24"><rect x="2" y="5" width="20" height="14" rx="1" fill="currentColor"/><path d="M2 6l10 7 10-7" fill="none" stroke="#1f7ea6" stroke-width="1.6"/></svg>
      </li>
      <li>brenvalegroup.com.au
        <svg viewBox="0 0 24 24"><circle cx="12" cy="12" r="9" fill="none" stroke="currentColor" stroke-width="2"/><path d="M3 12h18M12 3c3 3 3 15 0 18M12 3c-3 3-3 15 0 18" fill="none" stroke="currentColor" stroke-width="1.5"/></svg>
      </li>
    </ul>

    <p class="address">3/41 Corbett Lane Kellow Ridge NSW 2517 Australia</p>
  </section>

  <section class="card card--back" aria-label="Business card back">
    <div class="masthead">
      <div class="brand"><span>Brenvale</span><span class="brand__dot"></span></div>
      <p class="tagline">Commercial Water Filtration Equipment</p>
    </div>
  </section>
</main>
</body>
</html>
```